Tern Hollow Print and Mailing Services

We are looking for a website layout design for a direct print and mailing company which prints graphics, post cards, letters, does mailing and more.

Please see attached logo, as it will be used to match color scheme of website.

Current website:
www.ternhollowprintmail.com

Websites we like:
https://quillbaypressworks.com

Target Market(s)

Businesses / Media

Number of Pages Required

3 page

Font styles to use
Sans Serif

Requirements
Must have
• Color scheme to match logo

```html
<!DOCTYPE html>
<html lang="en">
<head>
<meta charset="utf-8">
<title>Tern Hollow Print and Mailing Services</title>
<link href="https://fonts.googleapis.com/css2?family=Oswald:wght@400;500&family=Open+Sans:wght@400;600;700&display=swap" rel="stylesheet">
<style>
:root{
  --blue:#0b5aa2;
  --blue-dark:#0a3f78;
  --navy:#082a52;
  --ink:#222;
  --muted:#555;
  --magenta:#e13a7c;
  --olive:#a6ae2c;
  --green:#1f9a4d;
  --cyan:#19a3db;
  --faq-bg:#07060c;
  --light:#f3f3f3;
  --white:#fff;
}
*{box-sizing:border-box;margin:0;padding:0}
html,body{width:1200px;height:3468px;overflow:hidden}
body{font-family:"Open Sans",Arial,sans-serif;color:var(--ink);background:var(--white);position:relative}
.section{position:absolute;left:0;width:1200px}
.heading{font-family:"Oswald",Arial,sans-serif;font-weight:400}
.btn{display:inline-block;background:var(--blue-dark);color:var(--white);font:700 10px "Open Sans",sans-serif;text-transform:uppercase;letter-spacing:.5px;padding:6px 14px;border-radius:2px}

/* hero */
.hero{top:0;height:485px;background:linear-gradient(120deg,#3d4a55 0%,#6f7b83 35%,#2c3a46 60%,#7a8a96 100%);overflow:hidden}
.hero-photo{position:absolute;inset:0;background:radial-gradient(ellipse at 80% 75%,rgba(230,150,40,.55),transparent 40%),radial-gradient(ellipse at 25% 60%,rgba(200,210,215,.35),transparent 45%)}
.hero-shade{position:absolute;inset:0;background:linear-gradient(180deg,rgba(0,0,0,.35) 0%,rgba(0,0,0,0) 35%)}
.brand-box{position:absolute;left:150px;top:0;width:104px;height:88px;background:var(--white);box-shadow:0 2px 6px rgba(0,0,0,.3);display:flex;flex-direction:column;align-items:center;justify-content:center;text-align:center}
.brand-name{font:700 17px/1 "Open Sans",sans-serif;color:var(--blue-dark)}
.brand-sub{font:400 7px/1.2 "Open Sans",sans-serif;color:var(--blue-dark);margin-top:5px}
.main-nav{position:absolute;top:35px;left:372px;display:flex;gap:15px;font:400 10.5px "Oswald",sans-serif;color:var(--white);white-space:nowrap}
.main-nav .active{border-bottom:2px solid var(--white);padding-bottom:3px}
.nav-note{position:absolute;top:30px;left:918px;color:var(--white);font:700 8px/1.2 "Open Sans",sans-serif;text-align:center;white-space:nowrap}
.nav-signin{position:absolute;top:32px;left:992px;background:var(--blue-dark);color:var(--white);font:700 9px "Open Sans",sans-serif;padding:5px 14px;white-space:nowrap}
.hero-title{position:absolute;left:150px;top:228px;font:400 33px/1.2 "Oswald",sans-serif;color:var(--white);width:420px}
.login{position:absolute;left:768px;top:155px;width:284px;height:231px;background:var(--white);box-shadow:0 2px 10px rgba(0,0,0,.35)}
.login-tabs{display:flex;height:40px;font:600 9px "Open Sans",sans-serif;text-transform:uppercase}
.login-tabs span{flex:1;display:flex;align-items:center;justify-content:center}
.login-tabs .off{background:#e4e4e4;color:#777}
.login-tabs .on{color:var(--blue-dark);border-bottom:2px solid var(--blue-dark)}
.login-body{padding:14px 28px}
.login-lead{font-size:11px;color:var(--muted);margin-bottom:10px}
.field{height:28px;border:1px solid #ccc;border-radius:2px;font-size:9px;color:#777;padding:8px;margin-bottom:8px}
.keep{font-size:8px;color:#666;display:flex;align-items:center;gap:5px;margin-bottom:8px}
.keep i{width:9px;height:9px;border:1px solid #aaa;display:inline-block}
.login-row{display:flex;align-items:center;gap:14px;font-size:8px;color:#666}

/* about */
.about{top:485px;height:370px}
.about-photo{position:absolute;left:150px;top:54px;width:435px;height:266px;border-radius:4px;background:linear-gradient(135deg,#2b2f35,#6a6e74 40%,#c9a0c4 60%,#3aa0c8 80%,#1d2226)}
.about-title{position:absolute;left:615px;top:50px;font-size:22px;color:var(--blue-dark)}
.about-text{position:absolute;left:615px;top:84px;width:430px;font-size:11.2px;line-height:1.55;color:var(--muted)}
.about-text p+p{margin-top:12px}
.about .btn{position:absolute;left:615px;top:293px}

/* services */
.services{top:855px;height:486px;background:linear-gradient(180deg,#0a4e8e 0%,#0a3a6e 45%,#061d3c 100%);overflow:hidden}
.services-bg{position:absolute;inset:0;background:radial-gradient(ellipse at 50% 90%,rgba(60,120,200,.35),transparent 60%)}
.services-ghost{position:absolute;top:22px;width:100%;text-align:center;font:500 52px "Oswald",sans-serif;color:rgba(255,255,255,.08)}
.services-title{position:absolute;top:42px;width:100%;text-align:center;font-size:20px;color:var(--white)}
.arrow{position:absolute;top:42px;width:28px;height:28px}
.card{position:absolute;top:109px;width:208px;height:303px;border-radius:4px;color:var(--white);text-align:center;padding:0 14px}
.card svg{margin-top:32px}
.card h3{font:400 16px/1.25 "Oswald",sans-serif;margin-top:36px;height:42px;display:flex;align-items:center;justify-content:center}
.card p{font-size:10.5px;line-height:1.45;margin-top:12px;height:86px}
.card .more{font:700 13px "Open Sans",sans-serif;margin-top:12px}
.c1{left:150px;background:var(--magenta)}
.c2{left:381px;background:var(--olive)}
.c3{left:613px;background:var(--green)}
.c4{left:842px;background:var(--cyan)}
.services .ghost-btn{position:absolute;left:565px;top:440px;background:var(--white);color:var(--blue-dark);font:700 9px "Open Sans",sans-serif;padding:5px 18px}

/* news */
.news{top:1341px;height:925px}
.news-title{position:absolute;top:46px;width:100%;text-align:center;font-size:21px;color:var(--blue-dark)}
.ph{position:absolute}
.ph-1{left:250px;top:116px;width:335px;height:272px;background:linear-gradient(160deg,#6e7b86,#c6d3dd 45%,#3e9fd0 70%,#2b3440)}
.ph-2{left:615px;top:485px;width:333px;height:139px;background:linear-gradient(90deg,#e4e13b 0%,#e9e9e9 20%,#ea4a92 40%,#36b0d9 60%,#e6e6e6 80%,#3d3f44 100%)}
.ph-3{left:615px;top:661px;width:155px;height:160px;background:linear-gradient(150deg,#20353d,#8aa0a8 60%,#e3e7ea)}
.ph-4{left:798px;top:661px;width:152px;height:160px;background:linear-gradient(150deg,#2c2f33,#8c8f93 50%,#c2503f 80%,#3b3c40)}
.news-card{position:absolute;width:338px;background:var(--white);box-shadow:0 2px 14px rgba(0,0,0,.2);padding:24px 28px}
.news-card h3{font:400 19px/1.2 "Oswald",sans-serif;color:var(--blue);width:170px}
.news-card .date{font:700 11px/1.3 "Open Sans",sans-serif;margin-top:12px}
.news-card .lead{font:700 11px/1.45 "Open Sans",sans-serif;margin-top:10px}
.news-card .body{font-size:10px;line-height:1.55;color:var(--muted);margin-top:12px}
.news-card .btn{margin-top:18px}
.nc-1{left:615px;top:116px;height:335px}
.nc-2{left:250px;top:485px;height:330px}
.news .show-more{position:absolute;left:565px;top:864px}

/* faq */
.faq{top:2266px;height:513px;background:radial-gradient(ellipse at 50% 55%,#3a1748 0%,#170a22 30%,var(--faq-bg) 60%)}
.faq-title{position:absolute;top:50px;width:100%;text-align:center;font-size:20px;color:var(--white)}
.faq-sub{position:absolute;top:100px;width:100%;text-align:center;font-size:19px;color:var(--white)}
.faq-col{position:absolute;top:159px;width:436px;display:flex;flex-direction:column;gap:18px}
.faq-col.left{left:150px}
.faq-col.right{left:613px}
.q{height:35px;background:var(--white);border-radius:2px;display:flex;align-items:center;justify-content:space-between;padding:0 14px;font:600 10px "Open Sans",sans-serif;color:#333}
.q b{font-size:14px;font-weight:400}
.q.open{background:var(--blue);color:var(--white)}
.answer{margin-top:-18px;background:var(--white);padding:12px 14px;font-size:10px;line-height:1.5;color:var(--muted);height:66px}
.faq .see-more{position:absolute;left:565px;top:444px;background:var(--blue)}

/* contact */
.contact{top:2779px;height:499px}
.contact-panel{position:absolute;left:0;top:0;width:599px;height:499px;background:var(--blue)}
.contact-title{position:absolute;left:160px;top:30px;font-size:30px;line-height:1.2;color:var(--white)}
.contact-intro{position:absolute;left:160px;top:80px;width:428px;font-size:10px;line-height:1.55;color:var(--white)}
.contact-intro p+p{margin-top:8px}
.form{position:absolute;left:160px;top:160px;width:410px;color:var(--white);font-size:9px;line-height:1.3}
.row{display:flex;gap:18px;margin-bottom:10px}
.row>div{flex:1}
.input{height:22px;background:var(--white);border-radius:2px;margin-top:3px}
.radio{display:flex;align-items:center;gap:10px}
.radio i{width:12px;height:12px;background:var(--white);display:inline-block;border-radius:2px}
.radio .x{background:var(--white);position:relative}
.radio .x::after{content:"";position:absolute;left:3px;top:3px;width:6px;height:6px;border-radius:50%;background:#d23}
.area{height:68px;background:var(--white);margin-top:3px}
.form-btns{display:flex;gap:14px;margin-top:18px}
.form-btns span{background:var(--white);color:var(--blue-dark);font:700 9px "Open Sans",sans-serif;padding:6px 18px}
.map{position:absolute;left:599px;top:0;width:601px;height:499px;background:linear-gradient(135deg,#e6e6e3,#f2f2ef 50%,#e3e5e2)}
.map-tip{position:absolute;left:200px;top:176px;background:var(--white);box-shadow:0 1px 4px rgba(0,0,0,.3);font-size:10px;padding:10px 14px;color:#333}
.map-pin{position:absolute;left:312px;top:225px}

/* footer */
.footer{top:3278px;height:190px;background:var(--white)}
.foot-brand{position:absolute;left:150px;top:36px;width:160px;text-align:center}
.foot-brand .brand-name{font-size:20px}
.foot-divider{position:absolute;left:330px;top:20px;width:1px;height:140px;background:#ccc}
.key-title{position:absolute;left:352px;top:30px;font:700 14px "Open Sans",sans-serif;color:var(--blue-dark)}
.contacts{position:absolute;top:62px;display:flex;flex-direction:column;gap:10px;font-size:8px;line-height:1.35;color:#444}
.contacts.c-a{left:352px}
.contacts.c-b{left:588px}
.contact-item{display:flex;gap:6px}
.contact-item svg{flex:none;margin-top:1px}
.foot-links{position:absolute;left:822px;top:30px;width:230px;font-size:8px;line-height:1.9;color:#444}
.foot-links b{color:var(--ink)}
.copy{margin-top:8px;color:#666}
</style>
</head>
<body>

<header class="section hero">
  <div class="hero-photo" role="img" aria-label="Close-up of a digital printing press with colour proofs"></div>
  <div class="hero-shade"></div>
  <div class="brand-box">
    <div class="brand-name">Tern Hollow</div>
    <div class="brand-sub">Print and Mailing</div>
  </div>
  <nav class="main-nav">
    <span class="active">Home</span><span>About Us</span><span>Quotes &amp; Custom Orders</span><span>Services &amp; Print Products</span><span>News</span><span>My Invoice Account</span><span>FAQ</span><span>Contact Us</span>
  </nav>
  <div class="nav-note">CURRENT CLIENTS<br>&amp; NEW CLIENTS</div>
  <div class="nav-signin">SIGN IN</div>
  <h1 class="hero-title">Masters of Vibrant Color Digital Print and Mailing Services!</h1>
  <div class="login">
    <div class="login-tabs"><span class="off">I am a new customer</span><span class="on">I am an existing customer</span></div>
    <div class="login-body">
      <p class="login-lead">Sign-in to get custom quotes and orders.</p>
      <div class="field">Email</div>
      <div class="field">Password</div>
      <div class="keep"><i></i>Keep me logged in</div>
      <div class="login-row"><span class="btn">Login</span><span>Forgot password?</span></div>
    </div>
  </div>
</header>

<section class="section about">
  <div class="about-photo" role="img" aria-label="Colour ink cartridges labelled black, cyan, magenta and yellow"></div>
  <h2 class="heading about-title">About Us</h2>
  <div class="about-text">
    <p>Even in today's <b>digital marketplace</b>, mail continues to be one of the most effective forms of communication. Tern Hollow's mastery of the complexities of managed mail gives our clients the assurance that their mailings will be handled in the most professional, cost-effective, and efficient way possible. That means rapid results without the worry. You'll always get the optimum postage rates with our help. We'll even provide affordable mailing lists with advanced demographic filters to get you started on a successful campaign.</p>
    <p>And we don't stop there. Tern Hollow extends our expertise to laser and color digital printing, email and data management, fulfillment and graphic design services, offering everything you need to take your business to the top and keep it there.</p>
  </div>
  <span class="btn">Learn more</span>
</section>

<section class="section services">
  <div class="services-bg" role="img" aria-label="Night city skyline in blue tones"></div>
  <div class="services-ghost">Services &amp; Print Products</div>
  <h2 class="heading services-title">Services &amp; Print Products</h2>
  <svg class="arrow" style="left:150px" viewBox="0 0 28 28"><circle cx="14" cy="14" r="12.5" fill="none" stroke="#fff" stroke-width="1.5"/><path d="M16 9l-5 5 5 5" fill="none" stroke="#fff" stroke-width="1.8"/></svg>
  <svg class="arrow" style="left:1022px" viewBox="0 0 28 28"><circle cx="14" cy="14" r="12.5" fill="none" stroke="#fff" stroke-width="1.5"/><path d="M12 9l5 5-5 5" fill="none" stroke="#fff" stroke-width="1.8"/></svg>

  <article class="card c1">
    <svg width="34" height="34" viewBox="0 0 34 34"><path d="M8 4h15l5 5v21H8z" fill="none" stroke="#fff" stroke-width="2"/><path d="M12 13h12M12 18h12M12 23h8" stroke="#fff" stroke-width="2"/></svg>
    <h3>Lettershop Services</h3>
    <p>We handle your most complex mailing with integrated solutions including color ink jetting, intelligent inserting, specialty folding &amp; more.</p>
    <div class="more">More</div>
  </article>
  <article class="card c2">
    <svg width="34" height="34" viewBox="0 0 34 34"><path d="M8 4h15l5 5v21H8z" fill="none" stroke="#fff" stroke-width="2"/><path d="M12 13h12M12 18h12M12 23h8" stroke="#fff" stroke-width="2"/></svg>
    <h3>Mail Sorting</h3>
    <p>Our automated barcode sorting equipment reduces costs and speeds delivery while keeping you postal-compliant with all the postal changes and rules.</p>
    <div class="more">More</div>
  </article>
  <article class="card c3">
    <svg width="34" height="34" viewBox="0 0 34 34"><path d="M8 4h15l5 5v21H8z" fill="none" stroke="#fff" stroke-width="2"/><path d="M12 13h12M12 18h12M12 23h8" stroke="#fff" stroke-width="2"/></svg>
    <h3>Color Digital Printing Services</h3>
    <p>Develop an exciting one-to-one customer interaction with vibrant, full-color documents containing photos, artwork and names personalized to each customer.</p>
    <div class="more">More</div>
  </article>
  <article class="card c4">
    <svg width="34" height="34" viewBox="0 0 34 34"><path d="M8 4h15l5 5v21H8z" fill="none" stroke="#fff" stroke-width="2"/><path d="M12 13h12M12 18h12M12 23h8" stroke="#fff" stroke-width="2"/></svg>
    <h3>Fulfillment Services</h3>
    <p>Whenever your product and no matter how customized the order, our streamlined operation provides prompt, seamless and affordable services.</p>
    <div class="more">More</div>
  </article>
  <span class="ghost-btn">ALL SEE</span>
</section>

<section class="section news">
  <h2 class="heading news-title">News</h2>
  <div class="ph ph-1" role="img" aria-label="Large-format printer with ink lines"></div>
  <article class="news-card nc-1">
    <h3>Lorem Ipsum is simply dummy</h3>
    <p class="date">29,30 March 2018<br>Lorem Ipsum is simply dummy</p>
    <p class="lead">Lorem Ipsum is simply dummy text of the printing and typesetting industry.</p>
    <p class="body">Lorem Ipsum has been the industry's standard dummy text ever since the 1500s, when an unknown printer took a galley of type and scrambled it to make a type specimen book. Lorem Ipsum has been the industry's standard dummy text ever since the 1500s, when an unknown printer took a galley of type and scrambled it to make a type specimen book.</p>
    <span class="btn">Read more</span>
  </article>
  <article class="news-card nc-2">
    <h3>Lorem Ipsum is simply dummy</h3>
    <p class="date">29,30 March 2018<br>Lorem Ipsum is simply dummy</p>
    <p class="lead">Lorem Ipsum is simply dummy text of the printing and typesetting industry.</p>
    <p class="body">Lorem Ipsum has been the industry's standard dummy text ever since the 1500s, when an unknown printer took a galley of type and scrambled it to make a type specimen book. Lorem Ipsum has been the industry's standard dummy text ever since the 1500s, when an unknown printer took a galley of type and scrambled it to make a type specimen book.</p>
    <span class="btn">Read more</span>
  </article>
  <div class="ph ph-2" role="img" aria-label="Row of colourful printer ink tanks"></div>
  <div class="ph ph-3" role="img" aria-label="Printed labels running through a press"></div>
  <div class="ph ph-4" role="img" aria-label="Offset printing rollers"></div>
  <span class="btn show-more">Show more</span>
</section>

<section class="section faq">
  <h2 class="heading faq-title">FAQ'S</h2>
  <h3 class="heading faq-sub">General information</h3>
  <div class="faq-col left">
    <div class="q">Q. Why do I need to register or login to receive a quote or place an order?<b>+</b></div>
    <div class="q">Is your website secure?<b>+</b></div>
    <div class="q open">What type of file must I send for print orders?<b>−</b></div>
    <div class="answer">We can accept most types of art files. We prefer high-resolution PDFs, whereby you attach the native files, the fonts and any other special attachments that make up your art file.</div>
    <div class="q">Can I order a print and not mail?<b>+</b></div>
  </div>
  <div class="faq-col right">
    <div class="q">At what DPI should my images be?<b>+</b></div>
    <div class="q">How do I provide my files for full color digital printing?<b>+</b></div>
    <div class="q">How do I size my artwork if it has bleeds?<b>+</b></div>
    <div class="q">Where is Tern Hollow located?<b>+</b></div>
  </div>
  <span class="btn see-more">See more</span>
</section>

<section class="section contact">
  <div class="contact-panel">
    <h2 class="heading contact-title">Contact Us</h2>
    <div class="contact-intro">
      <p>Tern Hollow is happy to answer any questions about our printing and mailing services. Please call us directly or fill out the form below and we will get back to you immediately.</p>
      <p>We look forward to hearing from you!</p>
    </div>
    <div class="form">
      <div class="row"><div>Full Name<div class="input"></div></div><div>Email Address<div class="input"></div></div></div>
      <div class="row"><div>Company Name<div class="input"></div></div></div>
      <div class="row"><div class="radio">Current Customer <i></i> Yes <i class="x"></i> No</div></div>
      <div class="row"><div>Email<div class="input"></div></div><div>Tel<div class="input"></div></div></div>
      <div class="row"><div>Message<div class="area"></div></div></div>
      <div class="form-btns"><span>SUBMIT</span><span>RESET</span></div>
    </div>
  </div>
  <div class="map" role="img" aria-label="Street map around the office location">
    <div class="map-tip">ABC, Street City, Street City 12345</div>
    <svg class="map-pin" width="18" height="26" viewBox="0 0 18 26"><path d="M9 0a9 9 0 0 1 9 9c0 7-9 17-9 17S0 16 0 9a9 9 0 0 1 9-9z" fill="#1f5f9e"/><circle cx="9" cy="9" r="3.5" fill="#fff"/></svg>
  </div>
</section>

<footer class="section footer">
  <div class="foot-brand">
    <div class="brand-name">Tern Hollow</div>
    <div class="brand-sub">Print and Mailing</div>
  </div>
  <div class="foot-divider"></div>
  <h4 class="key-title">Key Contacts</h4>
  <div class="contacts c-a">
    <div class="contact-item"><svg width="11" height="8" viewBox="0 0 11 8"><rect width="11" height="8" fill="#1f5f9e"/><path d="M0 0l5.5 4L11 0" stroke="#fff" fill="none"/></svg><span>Marisol Vance - Company Founder and President<br>Email: mvance@ternhollowprintmail.com</span></div>
    <div class="contact-item"><svg width="11" height="8" viewBox="0 0 11 8"><rect width="11" height="8" fill="#1f5f9e"/><path d="M0 0l5.5 4L11 0" stroke="#fff" fill="none"/></svg><span>Theo Harlan - Chief Financial &amp; Operating Officer<br>Email: tharlan@ternhollowprintmail.com</span></div>
    <div class="contact-item"><svg width="11" height="8" viewBox="0 0 11 8"><rect width="11" height="8" fill="#1f5f9e"/><path d="M0 0l5.5 4L11 0" stroke="#fff" fill="none"/></svg><span>Ines Calder - Operations Manager<br>Email: icalder@ternhollowprintmail.com</span></div>
  </div>
  <div class="contacts c-b">
    <div class="contact-item"><svg width="11" height="8" viewBox="0 0 11 8"><rect width="11" height="8" fill="#1f5f9e"/><path d="M0 0l5.5 4L11 0" stroke="#fff" fill="none"/></svg><span>Estimator<br>Email: estimates@ternhollowprintmail.com</span></div>
    <div class="contact-item"><svg width="11" height="8" viewBox="0 0 11 8"><rect width="11" height="8" fill="#1f5f9e"/><path d="M0 0l5.5 4L11 0" stroke="#fff" fill="none"/></svg><span>Billing Associate<br>Email: billing@ternhollowprintmail.com</span></div>
  </div>
  <div class="foot-links">
    <div><b>Home</b> | About Us | Quotes &amp; Custom Orders |</div>
    <div>Services &amp; Print Products | News | My Invoice Account |</div>
    <div>FAQ | Contact Us</div>
    <div class="copy">© 2018 Tern Hollow Print and Mailing. All Rights Reserved.</div>
  </div>
</footer>

</body>
</html>
```